Marlowen

I'm looking for business cards with the logo I've attached. I don't have an specific idea in mind and open to anything. All the usual info will be involved. Name, position in company, nr, email, address

```html
<!DOCTYPE html>
<html lang="en">
<head>
<meta charset="utf-8">
<title>Marlowen Designs — Business Cards</title>
<link href="https://fonts.googleapis.com/css2?family=Questrial&family=Arimo:wght@400&display=swap" rel="stylesheet">
<style>
  :root {
    --navy: #1c3150;
    --gold: #f0b12f;
    --white: #ffffff;
    --ink: #1d1f24;
    --backdrop: #2a2a2c;
  }
  * { box-sizing: border-box; margin: 0; padding: 0; }
  html, body {
    width: 1200px; height: 900px; overflow: hidden;
    background: var(--backdrop);
  }
  .canvas { position: relative; width: 1200px; height: 900px; }

  .card {
    position: absolute;
    width: 700px; height: 400px;
    box-shadow: 0 18px 40px rgba(0,0,0,0.55);
    overflow: hidden;
  }

  /* Brand name: one font, one weight, one colour, with a plain dot */
  .brand-name {
    display: flex; align-items: center; gap: 16px;
    font-family: "Questrial", sans-serif;
    font-weight: 400;
    color: var(--gold);
    line-height: 1;
    white-space: nowrap;
  }
  .brand-dot {
    flex: none;
    border-radius: 50%;
    background: var(--gold);
  }

  /* Front */
  .card-front {
    left: 150px; top: 50px;
    background: var(--navy);
    display: flex; align-items: center; justify-content: center;
  }
  .card-front .brand-name { font-size: 50px; }
  .card-front .brand-dot { width: 22px; height: 22px; }

  /* Back */
  .card-back {
    left: 350px; top: 450px;
    background: var(--white);
  }
  .card-back .brand-name {
    position: absolute; left: 190px; top: 92px; width: 400px;
    justify-content: center;
    font-size: 36px; gap: 12px;
  }
  .card-back .brand-dot { width: 16px; height: 16px; }

  .person {
    position: absolute; left: 150px; top: 236px; width: 240px; text-align: right;
  }
  .person-name {
    font-family: "Questrial", sans-serif;
    font-size: 32px; color: var(--navy); line-height: 1;
  }
  .person-role {
    font-family: "Questrial", sans-serif;
    font-size: 17px; color: var(--gold); margin-top: 4px;
  }

  .divider {
    position: absolute; left: 410px; top: 200px;
    width: 3px; height: 118px; background: var(--navy);
  }

  .contacts {
    position: absolute; left: 438px; top: 212px;
    list-style: none;
    font-family: "Arimo", sans-serif; font-size: 15px; color: var(--ink);
  }
  .contacts li { display: flex; align-items: center; height: 30px; }
  .contacts svg { width: 16px; height: 16px; margin-right: 14px; fill: var(--gold); flex: none; }

  .footer-band { position: absolute; left: 0; bottom: 0; width: 700px; height: 62px; }
  .address {
    position: absolute; left: 175px; bottom: 14px; width: 450px; text-align: center;
    font-family: "Arimo", sans-serif; font-size: 15px; color: var(--gold);
  }
</style>
</head>
<body>
<main class="canvas">

  <section class="card card-front" aria-label="Card front">
    <p class="brand-name"><span class="brand-dot" aria-hidden="true"></span>Marlowen Designs</p>
  </section>

  <section class="card card-back" aria-label="Card back">
    <p class="brand-name"><span class="brand-dot" aria-hidden="true"></span>Marlowen Designs</p>

    <div class="person">
      <p class="person-name">Elias Varnholt</p>
      <p class="person-role">Manager</p>
    </div>

    <div class="divider"></div>

    <ul class="contacts">
      <li>
        <svg viewBox="0 0 24 24" aria-hidden="true"><path d="M6.6 10.8a15.1 15.1 0 0 0 6.6 6.6l2.2-2.2c.3-.3.7-.4 1-.2 1.1.4 2.3.6 3.6.6.6 0 1 .4 1 1V20c0 .6-.4 1-1 1A17 17 0 0 1 3 4c0-.6.4-1 1-1h3.5c.6 0 1 .4 1 1 0 1.3.2 2.5.6 3.6.1.3 0 .7-.2 1z"/></svg>
        014 5278 3960
      </li>
      <li>
        <svg viewBox="0 0 24 24" aria-hidden="true"><path d="M2 5h20v14H2zm2 2v.5l8 5 8-5V7zm0 2.9V17h16V9.9l-8 5z"/></svg>
        info@marlowendesigns.com
      </li>
      <li>
        <svg viewBox="0 0 24 24" aria-hidden="true"><path d="M12 2a10 10 0 1 0 0 20 10 10 0 0 0 0-20zm6.9 6h-3a15 15 0 0 0-1.3-3.7A8 8 0 0 1 18.9 8zM12 4c.8 1.1 1.5 2.5 1.9 4h-3.8c.4-1.5 1.1-2.9 1.900-4zM4.3 14a8 8 0 0 1 0-4h3.4a16 16 0 0 0 0 4zm.8 2h3a15 15 0 0 0 1.3 3.7A8 8 0 0 1 5.1 16zm3-8h-3a8 8 0 0 1 4.3-3.7C8.8 5.5 8.4 6.7 8.1 8zM12 20c-.8-1.1-1.5-2.5-1.9-4h3.8c-.4 1.5-1.1 2.9-1.9 4zm2.3-6H9.7a14 14 0 0 1 0-4h4.6a14 14 0 0 1 0 4zm.3 5.7c.6-1.1 1-2.4 1.3-3.7h3a8 8 0 0 1-4.3 3.7zm1.7-5.7a16 16 0 0 0 0-4h3.4a8 8 0 0 1 0 4z"/></svg>
        www.marlowendesigns.com
      </li>
    </ul>

    <svg class="footer-band" viewBox="0 0 700 62" aria-hidden="true">
      <rect x="0" y="40" width="168" height="4" fill="var(--gold)"/>
      <rect x="622" y="8" width="78" height="4" fill="var(--gold)"/>
      <polygon points="168,52 190,10 600,10 622,52" fill="var(--navy)"/>
      <rect x="0" y="52" width="700" height="10" fill="var(--navy)"/>
    </svg>
    <p class="address">24 Harlow Ridge Rd, Elmford NJ 07124, Suite 210</p>
  </section>

</main>
</body>
</html>
```